Kestrel Bridge Consulting (KBC) Business Card Design

I would like to create double-sided business cards that contain:
1) Name: Derek Molvane
2) Phone Number: +1 (555) 218-4907
3) Email: Derek.Molvane@KestrelBridgeConsulting.example
4) Website: KestrelBridgeConsulting.example

I would like to include my logo and a color scheme similar to the Varnholt Grand Prix Ostera squad color scheme (black, silver, greenish-blue – but can also include regular blue)

What we do: Our company develops and delivers innovative and pragmatic information technology and cybersecurity risk and compliance solutions for organizations in the commercial market as well as the federal, and state/local sectors.

```html
<!DOCTYPE html>
<html lang="en">
<head>
<meta charset="utf-8">
<title>Kestrel Bridge Consulting – Business Card</title>
<link rel="stylesheet" href="https://fonts.googleapis.com/css2?family=Montserrat:wght@400;500;600&display=swap">
<style>
  :root {
    --page: #e9e6e1;
    --card: #ffffff;
    --ink: #1c1c22;
    --teal: #3fb5b3;
    --blue: #1271b3;
    --blue-deep: #1a78bf;
    --teal-soft: #42b9b6;
    --white: #ffffff;
  }
  * { margin: 0; padding: 0; box-sizing: border-box; }
  html, body { width: 900px; height: 1200px; overflow: hidden; }
  body {
    position: relative;
    background: var(--page);
    font-family: "Montserrat", Arial, sans-serif;
    color: var(--ink);
  }
  .card {
    position: absolute;
    left: 80px;
    width: 742px;
    height: 442px;
    border-radius: 30px;
    overflow: hidden;
  }
  .card-front { top: 130px; background: var(--card); }
  .card-back { top: 637px; }

  .brand {
    position: absolute;
    display: flex;
    align-items: center;
    gap: 14px;
  }
  .brand-dot {
    width: 64px; height: 64px;
    border-radius: 50%;
    background: var(--teal);
    flex: none;
  }
  .brand-name {
    font-weight: 500;
    text-transform: uppercase;
    line-height: 1.02;
    letter-spacing: 0.5px;
  }
  .card-front .brand { left: 38px; top: 48px; }
  .card-front .brand-name { font-size: 25px; color: var(--ink); }

  .holder { position: absolute; left: 38px; top: 188px; }
  .holder-name { font-size: 26px; font-weight: 600; color: var(--teal); line-height: 1.15; }
  .holder-role { font-size: 16px; color: var(--ink); margin-top: 2px; }

  .contacts { position: absolute; left: 38px; top: 268px; list-style: none; }
  .contacts li { display: flex; align-items: center; gap: 9px; height: 21.5px; }
  .contacts svg { width: 14px; height: 14px; fill: var(--blue); flex: none; }
  .contact-phone { font-size: 16px; }
  .contact-email { font-size: 14px; }
  .contact-web { font-size: 16.5px; }

  .address-band {
    position: absolute; left: 0; top: 354px;
    width: 100%; height: 44px;
    background: linear-gradient(90deg, var(--blue) 0 86%, var(--teal-soft) 86% 100%);
  }
  .address-band p {
    color: var(--white); font-size: 16.5px;
    line-height: 44px; padding-left: 34px;
  }
  .band-seal {
    position: absolute; left: 582px; top: 338px;
    width: 76px; height: 76px; border-radius: 50%;
    background: var(--white);
  }

  .back-field {
    position: absolute; inset: 0;
    background: linear-gradient(125deg, var(--blue-deep) 0%, #2c9bc4 50%, var(--teal-soft) 100%);
  }
  .card-back .brand { left: 420px; top: 296px; gap: 10px; }
  .card-back .brand-dot { width: 54px; height: 54px; background: var(--white); }
  .card-back .brand-name { font-size: 17px; color: var(--white); }
</style>
</head>
<body>
  <section class="card card-front">
    <div class="brand">
      <span class="brand-dot"></span>
      <p class="brand-name">Kestrel Bridge<br>Consulting</p>
    </div>

    <div class="holder">
      <p class="holder-name">Derek Molvane</p>
      <p class="holder-role">Owner</p>
    </div>

    <ul class="contacts">
      <li class="contact-phone">
        <svg viewBox="0 0 16 16"><path d="M2 5c0-2 3-3 6-3s6 1 6 3v1h-3V5H5v1H2zM4 7h8l2 3v3H2v-3zm4 1.5a1.8 1.8 0 1 0 0 3.6 1.8 1.8 0 0 0 0-3.6z"/></svg>
        +1 (555) 218-4907
      </li>
      <li class="contact-email">
        <svg viewBox="0 0 16 16"><path d="M1 3h14v10H1zm1.5 1.3V5l5.5 3.6L13.5 5v-.7z"/></svg>
        Derek.Molvane@KestrelBridgeConsulting.example
      </li>
      <li class="contact-web">
        <svg viewBox="0 0 16 16"><path d="M8 1a7 7 0 1 0 0 14A7 7 0 0 0 8 1zm-1 2.2L5 6l2 1 1 3-2 2V9L4 7 3 5.4A5 5 0 0 1 7 3.2zm3 .3A5 5 0 0 1 13 8l-2 1-1-2 1-2z"/></svg>
        KestrelBridgeConsulting.example
      </li>
    </ul>

    <div class="address-band">
      <p>Kornblumenweg 18, 22761 Hamburg</p>
    </div>
    <span class="band-seal"></span>
  </section>

  <section class="card card-back">
    <div class="back-field" role="img" aria-label="Repeating brand pattern over a blue to teal gradient"></div>
    <div class="brand">
      <span class="brand-dot"></span>
      <p class="brand-name">Kestrel Bridge<br>Consulting</p>
    </div>
  </section>
</body>
</html>
```